Kid's Cancer Camp Business Card

Create a unique Two-Sided color business cards for Camp Willow Brook, a pediatric cancer camp.

The camp tag line is: Where brave kids find big summer smiles...

Dale Morrisey, Executive Director
Camp Willow Brook Charitable Foundation, Inc
PO Box 918
Harlow Falls, ME 06832

Phone - 203-555-0143
Fax - 203-555-0187
Email: dale@campwillowbrook.example
www.campwillowbrook.example

Target Market(s)

Potential Donors, Volunteers and Campers

Industry/Entity Type

Non-profit pediatric cancer camp

Contact Information for Business Card

All contact info that is included in the description

Font styles to use
Other font styles liked:
• Designer chooses font

Requirements
Must have
• Camp Willow Brook Logo and Tag Line
Nice to have
• should be eye catching
Should not have
• not cartoony

```html
<!DOCTYPE html>
<html lang="en">
<head>
<meta charset="utf-8">
<title>Camp Willow Brook – Business Card</title>
<link rel="stylesheet" href="https://fonts.googleapis.com/css2?family=Lato:wght@400;700&family=Lora:ital,wght@1,500&family=Montserrat:wght@700&display=swap">
<style>
  :root {
    --bg: #c9c9c9;
    --blue-deep: #0a66a0;
    --blue-mid: #0e7fa8;
    --teal: #05a4a0;
    --sun: #f9b224;
    --ink-blue: #1769a3;
    --ink: #1d1d1d;
    --white: #ffffff;
  }
  * { box-sizing: border-box; margin: 0; padding: 0; }
  html, body { width: 1200px; height: 900px; overflow: hidden; }
  body {
    background: var(--bg);
    font-family: "Lato", Arial, sans-serif;
    display: flex;
    flex-direction: column;
    align-items: center;
    justify-content: center;
    gap: 36px;
  }
  .card {
    width: 700px;
    height: 400px;
    border-radius: 34px;
    position: relative;
    overflow: hidden;
    box-shadow: 0 6px 18px rgba(0,0,0,0.22);
  }
  .brand {
    display: flex;
    align-items: center;
    gap: 14px;
    font-family: "Lato", Arial, sans-serif;
    font-weight: 700;
    white-space: nowrap;
  }
  .brand-dot { border-radius: 50%; background: var(--sun); flex: none; }

  /* Front */
  .card-front {
    background: linear-gradient(200deg, var(--teal) 0%, var(--blue-mid) 45%, var(--blue-deep) 100%);
    display: flex;
    flex-direction: column;
    align-items: center;
    justify-content: center;
    gap: 26px;
  }
  .card-front .brand { font-size: 54px; color: var(--white); }
  .card-front .brand-dot { width: 42px; height: 42px; }
  .tagline {
    font-family: "Montserrat", Arial, sans-serif;
    font-weight: 700;
    font-size: 19px;
    letter-spacing: 0.5px;
    text-transform: uppercase;
    color: var(--sun);
  }

  /* Back */
  .card-back {
    background: var(--white);
    display: grid;
    grid-template-columns: 1fr 1fr;
    column-gap: 20px;
    padding: 56px 44px 44px 50px;
  }
  .back-left { display: flex; flex-direction: column; justify-content: space-between; }
  .card-back .brand { font-size: 32px; color: var(--ink-blue); }
  .card-back .brand-dot { width: 26px; height: 26px; }
  .contact-list { list-style: none; display: flex; flex-direction: column; gap: 6px; }
  .contact-list li {
    display: flex; align-items: center; gap: 12px;
    font-size: 17px; color: var(--ink); white-space: nowrap;
  }
  .contact-list svg { width: 20px; height: 20px; flex: none; }
  .contact-list .web-domain { color: var(--ink-blue); }
  .back-right {
    display: flex; flex-direction: column; align-items: flex-end; text-align: right;
    justify-content: center; gap: 34px;
  }
  .person-name {
    font-family: "Lora", Georgia, serif; font-style: italic; font-weight: 500;
    font-size: 34px; color: var(--ink-blue); line-height: 1;
  }
  .person-title { font-size: 18px; color: var(--ink); margin-top: 6px; }
  .org-name {
    font-family: "Lora", Georgia, serif; font-style: italic; font-weight: 500;
    font-size: 21px; color: var(--ink-blue); line-height: 1.25;
  }
  .org-address { font-size: 18px; color: var(--ink); margin-top: 8px; white-space: nowrap; }
</style>
</head>
<body>

  <section class="card card-front" aria-label="Card front">
    <div class="brand"><span class="brand-dot"></span><span class="brand-name">Camp Willow Brook</span></div>
    <p class="tagline">Where brave kids find big summer smiles...</p>
  </section>

  <section class="card card-back" aria-label="Card back">
    <div class="back-left">
      <div class="brand"><span class="brand-dot"></span><span class="brand-name">Camp Willow Brook</span></div>
      <ul class="contact-list">
        <li>
          <svg viewBox="0 0 24 24" aria-hidden="true"><path fill="var(--sun)" d="M6.6 10.8a15 15 0 0 0 6.6 6.6l2.2-2.2a1 1 0 0 1 1-.25 11.4 11.4 0 0 0 3.6.57 1 1 0 0 1 1 1V20a1 1 0 0 1-1 1A17 17 0 0 1 3 4a1 1 0 0 1 1-1h3.5a1 1 0 0 1 1 1c0 1.25.2 2.45.57 3.57a1 1 0 0 1-.25 1z"/></svg>
          203-555-0143
        </li>
        <li>
          <svg viewBox="0 0 24 24" aria-hidden="true"><path fill="var(--sun)" d="M7 3h10v5H7zM4 9h16a2 2 0 0 1 2 2v6h-4v4H6v-4H2v-6a2 2 0 0 1 2-2zm4 7v3h8v-3z"/></svg>
          203-555-0187
        </li>
        <li>
          <svg viewBox="0 0 24 24" aria-hidden="true"><path fill="var(--sun)" d="M3 5h18v14H3zm2 2v.5l7 5 7-5V7l-7 5z"/></svg>
          dale@campwillowbrook.example
        </li>
        <li>
          <svg viewBox="0 0 24 24" aria-hidden="true"><g fill="none" stroke="var(--sun)" stroke-width="2"><circle cx="12" cy="12" r="9"/><path d="M3 12h18M12 3c3 3 3 15 0 18M12 3c-3 3-3 15 0 18"/></g></svg>
          <span>www.<span class="web-domain">campwillowbrook</span>.example</span>
        </li>
      </ul>
    </div>
    <div class="back-right">
      <div class="person">
        <p class="person-name">Dale Morrisey</p>
        <p class="person-title">Executive Director</p>
      </div>
      <div class="org">
        <p class="org-name">Camp Willow Brook Charitable<br>Foundation, Inc</p>
        <p class="org-address">PO Box 918, Harlow Falls, ME 06832</p>
      </div>
    </div>
  </section>

</body>
</html>
```